Yard sign for Chimney Buisness

I am looking for a 18 Tall x 24" wide yard sign design incorporating our logo/name. We want the signs to stand out and be readable from a distance. only want our logo/business name and website on the sign . www.tallowmerevt.com

Target Market(s)

homeowners

Requirements
Must have
• logo/buisness name
• website
• must be visable at a distance and readable

```html
<!DOCTYPE html>
<html lang="en">
<head>
<meta charset="utf-8">
<title>Tallowmere Hearth Yard Sign</title>
<link rel="stylesheet" href="https://fonts.googleapis.com/css2?family=Cinzel:wght@500&display=swap">
<style>
  :root {
    --backdrop: #363636;
    --sign-white: #ffffff;
    --ink: #2b2b2b;
    --brand-red: #a91b1b;
  }
  * { margin: 0; padding: 0; box-sizing: border-box; }
  html, body { width: 1200px; height: 1200px; overflow: hidden; }
  body {
    background: var(--backdrop);
    display: flex;
    align-items: center;
    justify-content: center;
    font-family: "Cinzel", "Times New Roman", serif;
  }
  .yard-sign {
    position: relative;
    width: 1040px;
    height: 780px;
    background: var(--sign-white);
    overflow: hidden;
  }
  .brand-name {
    position: absolute;
    top: 200px;
    left: 0;
    right: 0;
    text-align: center;
    font-size: 70px;
    font-weight: 500;
    color: var(--ink);
    letter-spacing: 2px;
    line-height: 1;
    white-space: nowrap;
  }
  .sign-bands {
    position: absolute;
    left: 0;
    top: 0;
    width: 1040px;
    height: 780px;
  }
  .band-dark { fill: var(--ink); }
  .band-red { fill: var(--brand-red); }
  .website {
    position: absolute;
    left: 0;
    right: 0;
    top: 676px;
    text-align: center;
    color: var(--sign-white);
    font-size: 36px;
    font-weight: 500;
    letter-spacing: 5px;
    text-transform: uppercase;
  }
</style>
</head>
<body>
  <main class="yard-sign">
    <svg class="sign-bands" viewBox="0 0 1040 780" aria-hidden="true">
      <path class="band-dark" d="M0,560 Q520,500 1040,560 L1040,780 L0,780 Z"/>
      <path class="band-red" d="M0,590 Q520,530 1040,590 L1040,780 L0,780 Z"/>
    </svg>
    <h1 class="brand-name">TALLOWMERE HEARTH</h1>
    <p class="website">www.tallowmerevt.com</p>
  </main>
</body>
</html>
```